Kesar tadka food truck catering business card

Need business card for indian restaurant - food truck- catering business
Updates

Reason: Just launched

Updated picture of new logo we need on business card

please see new LOGO in picture brief, need card with NEW LOGO

Industry/Entity Type

Indian Restaurant

Requirements
Must have
• Food truck. Catering

Owner Gurmeet Dhaliwal
Cell: 555-013-7284
Charleston,SC
www.KesarTadkaEats.com
www.plazaface.net/KesarTadkaEats

```html
<!DOCTYPE html>
<html lang="en">
<head>
<meta charset="utf-8">
<title>Kesar tadka — Business Card</title>
<link rel="stylesheet" href="https://fonts.googleapis.com/css2?family=Tinos:wght@400;700&display=swap">
<style>
  :root {
    --page-bg: #f7f7f7;
    --card-bg: #f0f0f0;
    --card-edge: #e8e8e8;
    --panel-top: #d6d6d6;
    --panel-bottom: #1e1e1e;
    --ink: #111111;
    --ink-shadow: rgba(0,0,0,0.35);
    --logo-ink: #ffffff;
    --accent: #d9b27c;
    --dots-light: #ffffff;
    --dots-mid: #e2e2e2;
  }
  * { box-sizing: border-box; margin: 0; padding: 0; }
  html, body {
    width: 1200px; height: 1000px; overflow: hidden;
    background: var(--page-bg);
  }
  .business-card {
    position: absolute;
    left: 200px; top: 277px;
    width: 785px; height: 421px;
    background: var(--card-bg);
    box-shadow: 2px 3px 4px rgba(0,0,0,0.35);
    font-family: "Tinos", "Times New Roman", serif;
    overflow: hidden;
  }
  .edge-strip {
    position: absolute; left: 0; top: 0;
    width: 38px; height: 421px;
    background: var(--card-edge);
  }
  .brand-panel {
    position: absolute; left: 38px; top: 0;
    width: 219px; height: 393px;
    background: linear-gradient(to bottom, var(--panel-top) 0%, #9a9a9a 35%, #4a4a4a 70%, var(--panel-bottom) 100%);
  }
  .brand-lockup {
    position: absolute; left: 0; right: 0; top: 148px;
    text-align: center; color: var(--logo-ink);
  }
  .brand-mark {
    display: block;
    width: 30px; height: 30px; margin: 0 auto 10px;
    border-radius: 50%;
    background: var(--accent);
  }
  .brand-name {
    font-size: 36px; font-weight: 400; line-height: 1;
    white-space: nowrap;
  }
  .brand-tagline {
    margin-top: 8px;
    font-size: 15px; font-weight: 700;
  }
  .halftone-field {
    position: absolute; left: 257px; top: 0;
    width: 528px; height: 421px;
    background:
      radial-gradient(ellipse at 75% 95%, var(--dots-light) 0%, rgba(255,255,255,0) 60%),
      radial-gradient(ellipse at 100% 40%, var(--dots-light) 0%, rgba(255,255,255,0) 45%),
      linear-gradient(165deg, var(--card-bg) 0%, var(--dots-mid) 50%, var(--dots-light) 100%);
  }
  .contact-block {
    position: absolute; left: 257px; top: 0;
    width: 528px; height: 421px;
    display: flex; flex-direction: column; align-items: center;
    padding-top: 108px;
    color: var(--ink);
    text-shadow: 2px 2px 3px var(--ink-shadow);
  }
  .contact-block > div {
    transform: scaleX(0.84);
    white-space: nowrap;
  }
  .owner-name { font-size: 41px; line-height: 50px; }
  .contact-line { font-size: 31px; line-height: 47px; }
  .services-line { font-size: 24px; line-height: 38px; margin-top: 4px; }
  .social-line { font-size: 22px; line-height: 30px; }
</style>
</head>
<body>
  <div class="business-card">
    <div class="edge-strip"></div>
    <div class="brand-panel">
      <div class="brand-lockup">
        <span class="brand-mark"></span>
        <div class="brand-name">Kesar tadka</div>
        <div class="brand-tagline">Indian Street Food</div>
      </div>
    </div>
    <div class="halftone-field" role="img" aria-label="Light grey halftone dot pattern background"></div>
    <div class="contact-block">
      <div class="owner-name">Owner Gurmeet Dhaliwal</div>
      <div class="contact-line">Charleston,SC</div>
      <div class="contact-line">Cell: 555-013-7284</div>
      <div class="contact-line">WWW. KesarTadkaEats.com</div>
      <div class="services-line">Food Truck &#183; Catering</div>
      <div class="social-line">www.plazaface.net/KesarTadkaEats</div>
    </div>
  </div>
</body>
</html>
```